Bright Path Flyer Design for Virtual Online Clinic. -5.5 x 8.5 inches (half sheet)

We need a clean, modern flyer design for Bright Path, a new virtual walk-in clinic based in British Columbia. The flyer will be used in libraries, pharmacies, and community centers to help residents easily access primary care through their Bright Path NFC access card.
The flyer will ask a question : NEED A DOCTOR? This should be large and attention grabbing.
The design should clearly feature a Bright Path card image (the access card) as the centerpiece and visually show how patients can use it to book appointments. The tone should feel trustworthy, healthcare-oriented, and community-friendly — clean fonts, clear spacing, and strong readability from a distance.

Side One: This card has the NFC Access Card.
NEED A DOCTOR? (Large Font, Attention Grabbing)
How to Book an Appointment using your Bright Path Card
Step 1: Tap Your Card on Your Phone
Hold your card near the back of your phone.
It will activate automatically — no app needed.
The Bright Path scheduler will open.
Step 2: Schedule Your Appointment
Select your clinical concern.
Choose your time window.
Register (only once).
Confirm your appointment.
Step 3: Relax, we’ll take care of the rest
A doctor will call during your scheduled time.
Once booked, you’ll be able to call our office.
No emails, no texts — just a real person.
It’s that simple.
Side Two:
About Bright Path
Created by Dr. Marcus Ferrigan
Bright Path was founded to make healthcare simple and convenient. Prescription renewals. Common infections. Medical notes. And so much more.
Our doctors can address 120+ health concerns virtually — providing quality care without the waiting room. No waiting rooms. Just real doctors providing real care.
Why Patients Choose Bright Path
Easy access – book and be seen from anywhere in BC.
Effortless booking – tap your Bright Path Card to begin.
Trusted physicians – every visit is with a licensed BC family doctor.
How It Works
Book your visit — choose a time window that fits your day.
Join the queue — you’ll be called when it’s your turn.
Speak directly with your doctor — simple, secure, and stress-free.
Convenient Care for Common Concerns

Additional Details.
Please find the domain to be launched soon. I've attached the NFC card file for review, it is 85.5 mm x 54 mm. The card will be glued to the flyer.
I've attached examples of flyers but they are not the look I am seeking and I am looking for creative solutions.
Thank you!
http://brightpath-example.test/

Adult Patients in British Columbia

Healthcare

• Looking for clean lines, uniform appearance, and high legibility i.e poppins

0054AA
0677BA
7BADD7
CADEEF
E8F1F8

• Need A Doctor?
• Elegant style, not too busy, clear layout.
• Clutter, look cheap - review examples.

```html
<!DOCTYPE html>
<html lang="en">
<head>
<meta charset="utf-8">
<title>Bright Path Flyer</title>
<link href="https://fonts.googleapis.com/css2?family=Poppins:wght@500;600;700&family=Inter:wght@400;500&display=swap" rel="stylesheet">
<style>
  :root {
    --blue-deep: #0054AA;
    --blue-title: #1d5aa6;
    --blue-mid: #0677BA;
    --blue-soft: #7BADD7;
    --blue-pale: #CADEEF;
    --blue-wash: #E8F1F8;
    --ink: #22303f;
    --ink-soft: #2e3b4a;
    --page: #f8f9fa;
    --panel: #ffffff;
  }
  * { margin: 0; padding: 0; box-sizing: border-box; }
  html, body { width: 1200px; height: 812px; overflow: hidden; background: var(--page); }
  body { position: relative; font-family: "Inter", sans-serif; color: var(--ink); }

  .panel {
    position: absolute; top: 63px; width: 505px; height: 698px;
    background: var(--panel);
    box-shadow: 0 6px 18px rgba(30, 50, 80, 0.08);
  }
  .panel--front { left: 74px; }
  .panel--back { left: 633px; width: 507px; }

  /* Front */
  .headline {
    position: absolute; top: 44px; left: 0; width: 100%; text-align: center;
    font-family: "Poppins", sans-serif; font-weight: 600; font-size: 47px; line-height: 58px;
    color: var(--blue-title); letter-spacing: 0.5px;
  }
  .subhead {
    position: absolute; top: 107px; left: 0; width: 100%; text-align: center;
    font-size: 24px; line-height: 36px; color: var(--ink-soft);
  }
  .access-card {
    position: absolute; left: 131px; top: 215px; width: 257px; height: 166px;
    border-radius: 14px; background: linear-gradient(160deg, #fbfcfd, #f1f3f6);
    box-shadow: 0 4px 14px rgba(30, 50, 80, 0.14), 0 0 0 1px rgba(30,50,80,0.04);
    display: flex; align-items: center; justify-content: center; gap: 10px;
    padding-top: 36px;
  }
  .access-card__dot { width: 20px; height: 20px; border-radius: 50%; background: var(--blue-soft); }
  .access-card__name { font-family: "Inter", sans-serif; font-weight: 500; font-size: 24px; color: var(--blue-title); }

  .steps { position: absolute; left: 59px; top: 426px; list-style: none; }
  .step { display: flex; align-items: center; height: 49px; }
  .step__num {
    width: 30px; height: 30px; border-radius: 50%; flex: none;
    background: var(--blue-soft); border: 2px solid #5d9ad2; color: #fff;
    font-family: "Poppins", sans-serif; font-weight: 600; font-size: 18px;
    display: flex; align-items: center; justify-content: center; margin-right: 22px;
  }
  .step__text { font-size: 23px; color: var(--ink); }
  .signoff {
    position: absolute; top: 604px; left: 0; width: 100%; text-align: center;
    font-size: 31px; line-height: 40px; color: var(--ink);
  }

  /* Back */
  .back-title {
    position: absolute; top: 46px; left: 46px;
    font-family: "Poppins", sans-serif; font-weight: 600; font-size: 40px; line-height: 48px;
    color: var(--blue-title); letter-spacing: -0.5px;
  }
  .section-title { position: absolute; left: 46px; font-size: 22px; line-height: 28px; color: var(--ink); }
  .section-title--about { top: 115px; }
  .section-title--why { top: 284px; }
  .founder { position: absolute; top: 153px; left: 46px; font-size: 17px; line-height: 22px; color: var(--ink); }
  .about-text { position: absolute; top: 184px; left: 46px; width: 440px; font-size: 17px; line-height: 26px; color: var(--ink); }

  .reasons { position: absolute; left: 46px; top: 328px; list-style: none; }
  .reason { position: relative; padding-left: 40px; height: 67px; }
  .reason__icon { position: absolute; left: 0; top: 2px; width: 25px; height: 25px; }
  .reason__title { font-size: 19px; line-height: 28px; color: var(--ink); font-weight: 500; }
  .reason__text { font-size: 17px; line-height: 24px; color: var(--ink); }

  .concerns {
    position: absolute; left: 46px; top: 537px; width: 417px; height: 140px;
    background: var(--blue-wash); border-radius: 12px; padding: 14px 20px;
  }
  .concerns__title { font-size: 19px; line-height: 26px; color: var(--blue-deep); font-weight: 500; margin-bottom: 5px; }
  .concerns__list { font-size: 17px; line-height: 27px; color: var(--ink); }
</style>
</head>
<body>

<section class="panel panel--front">
  <h1 class="headline">NEED A DOCTOR?</h1>
  <p class="subhead">How to Book an Appointment<br>using your Bright Path Card</p>

  <div class="access-card">
    <span class="access-card__dot"></span>
    <span class="access-card__name">Bright Path</span>
  </div>

  <ol class="steps">
    <li class="step"><span class="step__num">1</span><span class="step__text">Tap Your Card on Your Phone</span></li>
    <li class="step"><span class="step__num">2</span><span class="step__text">Schedule Your Appointment</span></li>
    <li class="step"><span class="step__num">3</span><span class="step__text">Relax, we’ll take care of the rest</span></li>
  </ol>

  <p class="signoff">It’s that simple.</p>
</section>

<section class="panel panel--back">
  <h2 class="back-title">Healthcare, Simplified.</h2>

  <h3 class="section-title section-title--about">About Bright Path</h3>
  <p class="founder">Created by Dr. Marcus Ferrigan</p>
  <p class="about-text">Bright Path was founded to make healthcare simple and convenient, Prescription renewals, Common infections, Medical notes. And so much more.</p>

  <h3 class="section-title section-title--why">Why Patients Choose Bright Path</h3>
  <ul class="reasons">
    <li class="reason">
      <svg class="reason__icon" viewBox="0 0 26 26"><circle cx="13" cy="13" r="11.5" fill="none" stroke="#0677BA" stroke-width="1.8"/><path d="M7.5 13.3l3.8 3.7 7.2-7.5" fill="none" stroke="#0677BA" stroke-width="1.8" stroke-linecap="round" stroke-linejoin="round"/></svg>
      <p class="reason__title">Easy Access</p>
      <p class="reason__text">Book and be seen from anywhere in BC</p>
    </li>
    <li class="reason">
      <svg class="reason__icon" viewBox="0 0 26 26"><circle cx="13" cy="13" r="11.5" fill="none" stroke="#0677BA" stroke-width="1.8"/><path d="M7.5 13.3l3.8 3.7 7.2-7.5" fill="none" stroke="#0677BA" stroke-width="1.8" stroke-linecap="round" stroke-linejoin="round"/></svg>
      <p class="reason__title">Effortless Booking</p>
      <p class="reason__text">Tap your Bright Path Card to begin</p>
    </li>
    <li class="reason">
      <svg class="reason__icon" viewBox="0 0 26 26"><circle cx="13" cy="13" r="11.5" fill="none" stroke="#0677BA" stroke-width="1.8"/><path d="M7.5 13.3l3.8 3.7 7.2-7.5" fill="none" stroke="#0677BA" stroke-width="1.8" stroke-linecap="round" stroke-linejoin="round"/></svg>
      <p class="reason__title">Trusted Physicians</p>
      <p class="reason__text">Every visit is with a licensed BC family doctor</p>
    </li>
  </ul>

  <div class="concerns">
    <p class="concerns__title">Convenient Care for Common Concerns</p>
    <p class="concerns__list">Prescription Renewals – Common Infections<br>Medical Notes - Referrals - Skin Conditions<br>And much more...</p>
  </div>
</section>

</body>
</html>
```